Logo+Business Card Design for Architecture Photographer

Hi Everyone,

I am looking for logo/business designs for my new business - Dovel Pictura. My business does commercial photography with a specialization in architecture, luxury real estate, and design. The Int is short for interior and ex is short for exterior.

Some of the values of my business are:
- providing top quality photography and post-processing (straight lines, accurate and bold whites/blacks/colors) for commercial use (websites, social media, advertising campaigns)
- fostering a collaborative workflow that is professional and fun that will have clients returning because of the premium service they received
- asking the right questions so that I can capture what matters to my clients with my own creative vision

I want my final look to be modern and bold. The business cards will be letter pressed/debossed, so the design should incorporate that. I am imagining a solid matte olive green or matte navy blue background on one side and white on the other. The card will be printed on colored cards, so you don't have to put a colored background as part of the design. I have attached some examples of colors I like, although it doesn't matter too much for the purpose of your work.

I want the debossing to be part of the design of the business card. This debossing should be some some of pattern or a frame that holds the logo on the back of the card (I have attached some sample images named geometric debossing to show what I mean). Then I can just foil print my logo on the back. My contact info and a logo will be on the front.

Somewhere it should say "Architecture, Luxury Real Estate, Design".

My vision for the logo: no cameras or buildings. I can't think of anything symbolic for the logo, but it should somehow contain Dovel. It might be cool to have them separated by a line like Do | Vel. Or have the Int inside something, and the Ex outside.

I plan on using Quarvel to print the cards. You can find their specifications here: https://quarvel.example/products/duplex-business-cards?variant=5837204916273

It would be nice to have a psd file that I can edit as well as a PDF to deliver to the printing company. Both must be vector graphics.

Thank you to everyone who has submitted a design as it has helped me get a better idea of what I want.

Target Market(s)

Designers, architects

Industry/Entity Type

Photographer

Contact Information for Business Card

See project description

Logo Text

Dovel Pictura

Font styles to use
Sans Serif
Decorative

Colors
ffffff

Requirements
Must have
• Logo and business card design. Deboss area less than 3 square inches. Deboss area should be some sort of a pattern/design as shown in attachments labelled "Geometric Debossing Example".
• Logo design and deboss design must be submitted in vector graphics.
Nice to have
• Color doesn't have to be shown on the design because I will be printing on colored paper, although it would be helpful to help me visualize what it will eventually look like.
Should not have
• A camera or building in the design...too cliche.

```html
<!DOCTYPE html>
<html lang="en">
<head>
<meta charset="utf-8">
<title>Dovel Pictura — Business Card</title>
<link rel="stylesheet" href="https://fonts.googleapis.com/css2?family=Arimo:wght@400;700&display=swap">
<style>
  :root {
    --backdrop: #e9e7e3;
    --card-white: #f4f4f4;
    --card-black: #1f1f1f;
    --ink: #1c1c1c;
    --accent: #2aa8d4;
    --accent-band: #2b9fcb;
    --white: #ffffff;
    --deboss: #2c2c2c;
    --deboss-edge: #141414;
  }
  * { margin: 0; padding: 0; box-sizing: border-box; }
  html, body {
    width: 1200px; height: 780px; overflow: hidden;
    background: var(--backdrop);
    font-family: "Arimo", Arial, sans-serif;
  }
  .stage {
    position: relative; width: 1200px; height: 780px;
    display: flex; justify-content: center; align-items: center; gap: 120px;
  }
  .card {
    position: relative; width: 340px; height: 560px;
    box-shadow: 0 6px 18px rgba(0,0,0,.18);
    overflow: hidden;
  }
  .card-front { background: var(--card-white); color: var(--ink); }
  .card-back { background: var(--card-black); color: var(--white); }

  .brand { display: flex; align-items: center; gap: 10px; }
  .brand-name { font-weight: 700; letter-spacing: 1px; line-height: 1; white-space: nowrap; }
  .brand-dot { width: 20px; height: 20px; border-radius: 50%; background: var(--accent); flex: none; }

  .card-front .brand { position: absolute; top: 74px; left: 0; right: 0; justify-content: center; }
  .card-front .brand-name { font-size: 34px; color: var(--ink); }

  .person { position: absolute; top: 168px; left: 0; right: 0; text-align: center; }
  .person-name { font-size: 24px; font-weight: 700; }
  .person-role { font-size: 16px; color: var(--accent); margin-top: 2px; }

  .address { position: absolute; top: 242px; left: 0; right: 0; text-align: center; font-size: 16px; line-height: 1.35; }

  .contact { position: absolute; top: 310px; left: 36px; right: 36px; }
  .divider { position: relative; height: 20px; display: flex; align-items: center; }
  .divider::before { content: ""; position: absolute; left: 0; right: 0; top: 50%; height: 1px; background: var(--accent); }
  .divider-icon {
    position: relative; margin: 0 auto; width: 20px; height: 20px; border-radius: 50%;
    background: var(--accent); border: 2px solid var(--card-white);
    display: flex; align-items: center; justify-content: center;
  }
  .contact-line { text-align: center; font-size: 16px; margin: 6px 0; }

  .tagline {
    position: absolute; top: 428px; left: 0; right: 0; text-align: center;
    font-size: 11px; letter-spacing: 1.5px; text-transform: uppercase; color: var(--ink);
  }

  .social { position: absolute; top: 462px; left: 0; right: 0; display: flex; justify-content: center; gap: 10px; }
  .social-square { width: 20px; height: 20px; background: var(--accent); }

  .web-band {
    position: absolute; left: 0; right: 0; bottom: 0; height: 50px;
    background: var(--accent-band); color: var(--white);
    display: flex; align-items: center; justify-content: center;
    font-size: 17px; letter-spacing: 2px;
  }

  .deboss-frame { position: absolute; top: 80px; left: 70px; width: 200px; height: 400px; }

  .card-back .brand {
    position: absolute; top: 280px; left: 170px;
    transform: translate(-50%, -50%) rotate(90deg);
  }
  .card-back .brand-name { font-size: 52px; color: var(--white); }
  .card-back .brand-dot { width: 28px; height: 28px; }
</style>
</head>
<body>
<main class="stage">
  <section class="card card-front" aria-label="Business card front">
    <div class="brand">
      <span class="brand-name">Dovel Pictura</span>
      <span class="brand-dot"></span>
    </div>
    <div class="person">
      <p class="person-name">Mara Lindqvist</p>
      <p class="person-role">President</p>
    </div>
    <p class="address">PO BOX 48 Harbor Lane<br>7th street Larkfield</p>
    <div class="contact">
      <div class="divider"><span class="divider-icon">
        <svg width="10" height="10" viewBox="0 0 10 10" aria-hidden="true"><path d="M2 1 L4 1 L4.6 3 L3.5 4 Q4.5 6 6 6.5 L7 5.4 L9 6 L9 8 Q5 9.5 1 3.5 Z" fill="#fff"/></svg>
      </span></div>
      <p class="contact-line">555-014-2290</p>
      <div class="divider"><span class="divider-icon">
        <svg width="10" height="8" viewBox="0 0 10 8" aria-hidden="true"><rect x="0.5" y="0.5" width="9" height="7" fill="none" stroke="#fff"/><path d="M0.5 0.5 L5 4.5 L9.5 0.5" fill="none" stroke="#fff"/></svg>
      </span></div>
      <p class="contact-line">hello@dovelpictura.example</p>
    </div>
    <p class="tagline">Architecture, Luxury Real Estate, Design</p>
    <div class="social">
      <span class="social-square"></span>
      <span class="social-square"></span>
      <span class="social-square"></span>
    </div>
    <div class="web-band">www.dovelpictura.example</div>
  </section>

  <section class="card card-back" aria-label="Business card back">
    <svg class="deboss-frame" viewBox="0 0 200 400" aria-hidden="true">
      <g fill="none" stroke-width="2">
        <rect x="1" y="1" width="198" height="398" stroke="var(--deboss)"/>
        <rect x="12" y="12" width="176" height="376" stroke="var(--deboss-edge)"/>
        <path d="M1 1 L12 12 M199 1 L188 12 M1 399 L12 388 M199 399 L188 388" stroke="var(--deboss)"/>
        <path d="M100 12 L188 70 M100 12 L12 70 M100 388 L188 330 M100 388 L12 330" stroke="var(--deboss)"/>
      </g>
    </svg>
    <div class="brand">
      <span class="brand-name">Dovel</span>
      <span class="brand-dot"></span>
    </div>
  </section>
</main>
</body>
</html>
```